Providing Back Office Solutions to Financial Advisors and Attorney Needs a Business Card Design

Need a Business Card Design that speaks to Financial Advisor and Attorneys. Some of the word that come to mind is Clean/Simple & Futuristic.

Industry/Entity Type

Business

```html
<!DOCTYPE html>
<html lang="en">
<head>
<meta charset="utf-8">
<title>Kairon Back Office Solutions — Business Card</title>
<link href="https://fonts.googleapis.com/css2?family=Open+Sans:wght@400;600;700&display=swap" rel="stylesheet">
<style>
  :root{
    --brand-blue:#1b5fa6;
    --brand-blue-soft:#d6e4f3;
    --ink-blue:#1d4f94;
    --card-white:#ffffff;
    --page-bg:#eceef1;
  }
  html,body{margin:0;padding:0;width:1200px;height:800px;overflow:hidden;background:var(--page-bg);}
  body{font-family:"Open Sans",Arial,sans-serif;position:relative;}
  .business-card{
    position:absolute;left:180px;top:160px;width:840px;height:480px;
    background:var(--card-white);box-shadow:0 6px 24px rgba(0,0,0,.12);overflow:hidden;
  }
  .name-ribbon{position:absolute;left:60px;top:0;width:170px;height:250px;}
  .name-ribbon svg{display:block}
  .holder{position:absolute;left:60px;top:78px;width:170px;text-align:center;color:#fff;}
  .holder-name{font-weight:700;font-size:24px;letter-spacing:.5px;line-height:1.1;}
  .holder-role{font-weight:400;font-size:21px;line-height:1.1;}
  .brand-mark{position:absolute;left:75px;top:275px;width:150px;height:150px;border-radius:50%;background:var(--brand-blue-soft);border:6px solid var(--brand-blue);box-sizing:border-box;}
  .brand-lockup{position:absolute;left:440px;top:105px;display:flex;align-items:center;gap:16px;color:var(--brand-blue);font-weight:600;}
  .brand-square{width:44px;height:44px;background:var(--brand-blue);}
  .brand-name{font-size:48px;letter-spacing:3px;line-height:1;}
  .brand-tagline{font-size:18px;letter-spacing:.5px;margin-top:6px;}
  .contact-list{position:absolute;left:365px;top:300px;margin:0;padding:0;list-style:none;color:var(--ink-blue);font-size:21px;}
  .contact-list li{display:flex;align-items:center;gap:14px;height:36px;}
  .contact-list svg{width:18px;height:18px;flex:none;}
</style>
</head>
<body>
  <article class="business-card">
    <div class="name-ribbon">
      <svg width="170" height="250" viewBox="0 0 170 250"><polygon points="0,0 170,0 170,200 85,250 0,200" fill="var(--brand-blue)"/></svg>
    </div>
    <div class="holder">
      <div class="holder-name">JOHN DOE</div>
      <div class="holder-role">manager</div>
    </div>
    <div class="brand-mark" role="img" aria-label="Brand symbol area"></div>

    <div class="brand-lockup">
      <div class="brand-square"></div>
      <div>
        <div class="brand-name">KAIRON</div>
        <div class="brand-tagline">BACK OFFICE SOLUTIONS</div>
      </div>
    </div>

    <ul class="contact-list">
      <li><svg viewBox="0 0 24 24"><path d="M6.6 10.8a15 15 0 0 0 6.6 6.6l2.2-2.2a1 1 0 0 1 1-.25 11.4 11.4 0 0 0 3.6.57 1 1 0 0 1 1 1V20a1 1 0 0 1-1 1A17 17 0 0 1 3 4a1 1 0 0 1 1-1h3.5a1 1 0 0 1 1 1c0 1.25.2 2.45.57 3.6a1 1 0 0 1-.25 1z" fill="var(--brand-blue)"/></svg>014 555 2870</li>
      <li><svg viewBox="0 0 24 24"><rect x="2.5" y="5" width="19" height="14" fill="none" stroke="var(--brand-blue)" stroke-width="2"/><path d="M3 6l9 7 9-7" fill="none" stroke="var(--brand-blue)" stroke-width="2"/></svg>email@kaironbackoffice.com</li>
      <li><svg viewBox="0 0 24 24"><circle cx="12" cy="12" r="10" fill="var(--brand-blue)"/><path d="M2 12h20M12 2c3 3 3 17 0 20M12 2c-3 3-3 17 0 20" fill="none" stroke="#fff" stroke-width="1.4"/></svg>www.kaironbackofficesolutions.com</li>
    </ul>
  </article>
</body>
</html>
```